Business Card Design

Please copy the format of the attached card.

FRONT:
White text small blue horses head logo where "mirun" in in example

BACK:
Blue background w/ white horses head

Industry/Entity Type

Business

Contact Information for Business Card

Calvin Ostrow
Chief Executive Officer
Halvern Lodges & Resorts
412 Lindmoor Street | San Francisco, California 94109
Tel: +1.555.482.1937
email: calvin@halvernlodges.example

```html
<!DOCTYPE html>
<html lang="en">
<head>
<meta charset="utf-8">
<title>Halvern Lodges &amp; Resorts — Business Card</title>
<link rel="stylesheet" href="https://fonts.googleapis.com/css2?family=Open+Sans:wght@400;600;700&display=swap">
<style>
  :root {
    --page-bg: #e9ebee;
    --card-white: #ffffff;
    --brand-blue: #2b5c9f;
    --brand-blue-deep: #2a5797;
    --text-blue: #2e5a96;
    --on-blue: #ffffff;
    --card-shadow: rgba(20, 30, 50, 0.18);
  }
  * { margin: 0; padding: 0; box-sizing: border-box; }
  html, body {
    width: 1200px;
    height: 900px;
    overflow: hidden;
    background: var(--page-bg);
    font-family: "Open Sans", Arial, sans-serif;
  }
  .canvas {
    width: 1200px;
    height: 900px;
    display: flex;
    flex-direction: column;
    align-items: center;
    justify-content: center;
    gap: 56px;
  }
  .card {
    position: relative;
    width: 630px;
    height: 360px;
    box-shadow: 0 6px 18px var(--card-shadow);
  }
  .card--back {
    background: linear-gradient(160deg, var(--brand-blue) 0%, var(--brand-blue-deep) 100%);
    display: flex;
    align-items: center;
    justify-content: center;
  }
  .card--front {
    background: var(--card-white);
    color: var(--text-blue);
  }
  .brand-mark {
    display: flex;
    align-items: center;
    gap: 10px;
    font-weight: 600;
    letter-spacing: 0.02em;
  }
  .brand-mark__dot {
    width: 14px;
    height: 14px;
    border-radius: 50%;
  }
  .card--back .brand-mark {
    color: var(--on-blue);
    font-size: 44px;
  }
  .card--back .brand-mark__dot { background: var(--on-blue); width: 18px; height: 18px; }
  .card--front .brand-mark {
    position: absolute;
    right: 70px;
    bottom: 70px;
    color: var(--brand-blue);
    font-size: 30px;
  }
  .card--front .brand-mark__dot { background: var(--brand-blue); }
  .contact {
    position: absolute;
    left: 50px;
    top: 46px;
    font-size: 14.5px;
    line-height: 1.45;
  }
  .identity {
    position: absolute;
    left: 50px;
    top: 140px;
    font-size: 15px;
    line-height: 1.4;
  }
  .identity__name {
    font-weight: 700;
    font-size: 19px;
    margin-bottom: 2px;
  }
</style>
</head>
<body>
  <main class="canvas">
    <section class="card card--back" aria-label="Card back">
      <div class="brand-mark">
        <span class="brand-mark__dot"></span>
        <span class="brand-mark__name">mirun</span>
      </div>
    </section>

    <section class="card card--front" aria-label="Card front">
      <div class="contact">
        <p class="contact__address">412 Lindmoor Street | San Francisco, California 94109</p>
        <p class="contact__phone">Tel: +1.555.482.1937</p>
        <p class="contact__email">email: calvin@halvernlodges.example</p>
      </div>
      <div class="identity">
        <p class="identity__name">Calvin Ostrow</p>
        <p class="identity__title">Chief Executive Officer</p>
        <p class="identity__company">Halvern Lodges &amp; Resorts</p>
      </div>
      <div class="brand-mark">
        <span class="brand-mark__dot"></span>
        <span class="brand-mark__name">mirun</span>
      </div>
    </section>
  </main>
</body>
</html>
```